Real Estate Marketing Flyer-8.5 by 11 Dual Sided

This is Direct Marketing Flyer targeted to Condo Property owners
to list their condos/townhomes with us. We are looking for Stylish graphics with more upscale design and colors to standout from other agents in the marketplace.

We are open to how it is presented or any design choices made that make flyer standout/appealing.

Target Market(s)

Condo Property Owners..and to lesser extent buyers

Industry/Entity Type

Real Estate

Requirements
Must have
• First Page

Top

Banner with our Team Pic and Names Priscilla, Lou and Bea
(Insert a background photo of condominium complex of upper scale)

"Specializing in Condos/Townhomes"

Buying* Selling* Leasing* Short Sales

1 866 4Suite4 (784-8324)

www.BayviewSuiteGroup.com

When It's time to Sell, Lease of Buy
Contact us for FREE No Obligation Market Consultation

Select Recent Sales By The Bayview Suite Group

7182 W Hollander Ct. # B (688,698)

3 Bedroom 2.5 Bathroom *Represented Buyer*

4217 W Larkfield St. #41
(006,0176)

2 Bedroom 2.5 Bathroom *Water View*

814 S. Marrowbrook-23 2 Bedroom,2.5 Bathroom

3316 W. Loma Tranquila 2 Bedroom 2 Bathroom

26743 Fern Hollow 4 Bedroom 3 Bathrooms

Leasing-We Do That Too

Complete Landlord/Tenant Services

7461 Juniper (54.28)

2 Bedroom, 2 Bathroom

4219 W.Larkfield-38 1 Bedroom, 1 Bathroom

8027 E. Corvallo-216 3 Bedroom, 2.5 Bathroom

937 S. Trellis -D 2 Bedroom 2.5 Bathroom

News You Can Use

Consumer confidence reached a five-year high in May, according to a Merrow Council report also released on Tuesday, with big improvements in Americans’ views about both the current economy and future economic conditions. Consumer spending has also been strikingly resilient so far this year

The Dunmore-Wick 20-city composite index rose 10.9 percent over the last year, the biggest increase since April 2006. Several cities — Charlotte, N.C.; Los Angeles; Portland, Ore.; Seattle; and Tampa, Fla. — had their largest month-over-month gains in more than seven years.

Have you installed Carbon Monoxide detectors in Your Property?

As of July 1, 2011 the Household Air Safety Standards Act (Senate Bill - SB 472) requires owners of all single-family homes with an attached garage or a fossil fuel source to install carbon monoxide detectors within the home by July 1, 2011. Owners of multi-family leased or rental dwellings, such as apartment buildings, have until January 1, 2013 to comply with the law

Home Loan Relief Measure extended through 2013-The BayviewSuiteGroup has extensive experience doing Short Sales-call us for free consultation on doing a No Cost Short Sale.

The best way to cheer yourself up is to try to cheer somebody else up.
Edwin Harlow

Picture of Cute Dog and Cute Bea

We love Pets..When you buy or sell with TheBayviewSuiteGroup-we will make a donation to the animal shelter of your choice.

email contacts

lou@bayviewsuitegroup.com
bea@bayviewsuitegroup.com
priscilla@bayviewsuitegroup.com

(in very small print)

if your property is currently listed with a broker, this is not intention as a solicitation

Nice to have
• We provide cutting edge marketing along with good old fashioned service and hard work

Our "Total Outreach" program offers an overwhelming array of advertising designed to sell your property for top dollar and find the perfect buyer.

We also Provide Free Complete Home Staging consultation, Innovative Value Range Pricing options and so much more.

```html
<!DOCTYPE html>
<html lang="en">
<head>
<meta charset="utf-8">
<title>Leasing – The Bayview Suite Group</title>
<link href="https://fonts.googleapis.com/css2?family=Questrial&family=Mulish:ital,wght@0,400;0,800;1,800&display=swap" rel="stylesheet">
<style>
  :root {
    --orange: #f4511e;
    --orange-soft: #f47a4e;
    --orange-faint: #fbd3c6;
    --ink: #222222;
    --paper: #ffffff;
    --green-deep: #4c6b30;
    --green-mid: #6a8a40;
    --green-pale: #e3e9dc;
    --green-mist: #edf0e8;
  }
  * { margin: 0; padding: 0; box-sizing: border-box; }
  html, body { width: 927px; height: 1200px; overflow: hidden; background: var(--paper); }
  .flyer {
    position: relative; width: 927px; height: 1200px; overflow: hidden;
    font-family: "Questrial", sans-serif; color: var(--ink); background: var(--paper);
  }
  .ghost-word {
    position: absolute; left: -6px; top: 76px;
    font-size: 110px; letter-spacing: -3px; line-height: 1;
    color: var(--orange-faint);
  }
  .headline {
    position: absolute; left: 142px; top: 134px;
    font-size: 37px; font-weight: 400; letter-spacing: -0.5px;
    color: var(--orange); line-height: 1;
  }
  .service-band {
    position: absolute; left: 0; top: 168px; width: 927px; height: 27px;
    background: var(--orange);
  }
  .service-band span {
    position: absolute; left: 437px; top: 3px;
    color: var(--paper); font-size: 17px;
  }
  .photo-faded {
    position: absolute; left: 0; top: 195px; width: 423px; height: 473px;
    background: linear-gradient(180deg, var(--green-pale) 0%, var(--green-mist) 100%);
  }
  .photo-main {
    position: absolute; left: 423px; top: 195px; width: 504px; height: 473px;
    background: linear-gradient(180deg, var(--green-mid) 0%, var(--green-deep) 100%);
  }
  .listings {
    position: absolute; right: 537px; top: 225px; text-align: right;
    font-size: 17px; line-height: 21px;
  }
  .listing { margin-bottom: 24px; }
  .listing b { font-family: "Mulish", sans-serif; font-weight: 800; font-size: 15.5px; }
  .relief-note {
    position: absolute; right: 536px; top: 517px; width: 312px; text-align: right;
    font-size: 14.5px; line-height: 21.5px;
  }
  .news-band {
    position: absolute; left: 423px; top: 668px; width: 111px; height: 532px;
    background: var(--orange-soft); overflow: hidden;
  }
  .news-band .ghost {
    position: absolute; left: 8px; top: 640px; transform-origin: 0 0;
    transform: rotate(-90deg); font-size: 150px; line-height: 1;
    color: rgba(255,255,255,0.22); white-space: nowrap;
  }
  .news-band .title {
    position: absolute; left: 56px; top: 522px; transform-origin: 0 0;
    transform: rotate(-90deg); font-size: 55px; font-weight: 400; line-height: 1;
    color: var(--paper); white-space: nowrap;
  }
  .safety-note {
    position: absolute; right: 537px; top: 702px; width: 282px; text-align: right;
    font-size: 14.5px; line-height: 21.5px;
  }
  .safety-note p + p { margin-top: 21px; }
  .news-copy {
    position: absolute; left: 563px; top: 690px; width: 310px;
    font-size: 18.2px; line-height: 21.5px;
  }
  .news-copy p + p { margin-top: 21px; }
  .contacts {
    position: absolute; left: 45px; top: 1069px;
    font-size: 15px; line-height: 22px; font-family: "Mulish", sans-serif; font-style: italic;
  }
  .contacts h3 { font-weight: 800; font-size: 15px; }
  .disclaimer {
    position: absolute; left: 45px; top: 1168px;
    font-size: 8px; font-style: italic; font-family: "Mulish", sans-serif;
  }
</style>
</head>
<body>
<main class="flyer">
  <div class="ghost-word" aria-hidden="true">LEASING</div>
  <h1 class="headline">We Do That Too.</h1>
  <div class="service-band"><span>Complete Landlord/Tenant Services.</span></div>

  <div class="photo-faded" role="img" aria-label="Faded view of a landscaped condominium garden pond"></div>
  <div class="photo-main" role="img" aria-label="Condominium garden with a tree, tropical plants and a pond fountain"></div>

  <section class="listings">
    <div class="listing"><b>7461 Juniper (54.28)</b><br>2 Bedroom, 2 Bathroom</div>
    <div class="listing"><b>4219 W.Larkfield #38</b><br>1 Bedroom, 1 Bathroom</div>
    <div class="listing"><b>8027 E. Corvallo #216</b><br>3 Bedroom, 2.5 Bathroom</div>
    <div class="listing"><b>937 S. Trellis #D 2</b><br>Bedroom 2.5 Bathroom</div>
  </section>

  <p class="relief-note">Home Loan Relief Measure extended through 2013. The Bayview Suite Group has extensive experience doing Short Sales, call us for free consultation on doing a No Cost Short Sale.</p>

  <section class="safety-note">
    <p>Have you installed Carbon Monoxide detectors in Your Property?</p>
    <p>As of July 1, 2011 the Household Air Safety Standards Act (Senate Bill - SB 472) requires owners of all single-family homes with an attached garage or a fossil fuel source to install carbon monoxide detectors within the home by July 1, 2011. Owners of multi-family leased or rental dwellings, such as apartment buildings, have until January 1, 2013 to comply with the law</p>
  </section>

  <div class="news-band">
    <span class="ghost" aria-hidden="true">News</span>
    <h2 class="title">News You Can Use</h2>
  </div>

  <section class="news-copy">
    <p>Consumer confidence reached a five-year high in May, according to a Merrow Council report also released on Tuesday, with big improvements in Americans’ views about both the current economy and future economic conditions. Consumer spending has also been strikingly resilient so far this year.</p>
    <p>The Dunmore-Wick 20-city composite index rose 10.9 percent over the last year, the biggest increase since April 2006. Several cities — Charlotte, N.C.; Los Angeles; Portland, Ore.; Seattle; and Tampa, Fla. — had their largest month-over-month gains in more than seven years.</p>
  </section>

  <address class="contacts">
    <h3>Email:</h3>
    lou@bayviewsuitegroup.com<br>
    bea@bayviewsuitegroup.com<br>
    priscilla@bayviewsuitegroup.com
  </address>
  <p class="disclaimer">If your property is currently listed with a broker, this is not intention as a solicitation.</p>
</main>
</body>
</html>
```